User-interface and web design for new forum-style communication platform

We developed a new forum-style communication platform specially targetting stock investors to share and discuss information on companies listed on the stock exchange.

You have complete freedom for designing the user-interface and web design. Designs should include all features listed below.

Please read the attached document for full specifications. Also attached is a mockup of the layout, but this is only directional. A mockup for the user-profile is also attached, but does not need to be designed.

This project focusses on the homepage and thread view.

The winner(s) will be asked to design the complete project. (create thread box, user profile, registering, settings...)

We are looking for a well thought out, smart design that incorporates the specifications in the attached document. Please do not hesitate to contact us if anything is not clear.

Target Market(s)

Stock investors from 25 to 60 years old (the people that are currently on investor forums)

Industry/Entity Type

Communication

Font styles to use
Sans Serif

Colors

Designer to choose colors to be used in the design.

Requirements
Must have
• Full homepage design & Thread view specified in the attached document.
Nice to have
• Create thread view
- Field for adding tags
- field for subject of the thread
- text box with basic text editing
- method for sharing media
Should not have
• Logo design.

```html
<!DOCTYPE html>
<html lang="en">
<head>
<meta charset="utf-8">
<title>Company Name – Conversations</title>
<link href="https://fonts.googleapis.com/css2?family=Ubuntu:wght@400;500&family=Arimo:wght@400;700&display=swap" rel="stylesheet">
<style>
:root{
  --orange:#ff9c00;
  --orange-dark:#8a4a05;
  --white:#ffffff;
  --text-light:#e8e8e8;
  --muted:#9a9a9a;
  --band-dark:#2e2d2f;
  --band-mid:rgba(120,112,112,.75);
  --card:rgba(30,28,30,.88);
  --tagbar:#3b3a3c;
  --reply:#151416;
  --field:rgba(110,108,110,.8);
  --footer:#262526;
  --footer-bottom:#1c1b1c;
  --yellow:#f7d417;
}
*{box-sizing:border-box;margin:0;padding:0}
html,body{width:1200px;height:1172px;overflow:hidden}
body{position:relative;font-family:"Arimo",sans-serif;color:var(--text-light);
  background:radial-gradient(ellipse 420px 520px at 660px 360px,#6a5048 0%,transparent 70%),
  radial-gradient(ellipse 300px 200px at 760px 680px,#4e4e68 0%,transparent 70%),
  linear-gradient(180deg,#4a4647 0%,#3c3839 40%,#403a3a 70%,#4a4242 100%)}
.abs{position:absolute}
.ubuntu{font-family:"Ubuntu",sans-serif}

/* header */
.brand{left:150px;top:37px;display:flex;align-items:center;gap:12px;font-family:"Ubuntu",sans-serif;font-size:24px;color:var(--white)}
.brand-mark{width:42px;height:42px;border-radius:50%;background:var(--white)}
.search-main{left:422px;top:43px;width:515px;height:34px;border-radius:17px;background:var(--field);overflow:hidden;display:flex;align-items:center}
.search-main .q{flex:1;padding-left:46px;font-family:"Ubuntu",sans-serif;font-size:13px;color:var(--white)}
.search-main svg{position:absolute;left:14px;top:9px}
.btn-save{width:77px;height:34px;background:var(--orange);color:var(--white);font:500 12px "Ubuntu",sans-serif;display:flex;align-items:center;justify-content:center;border-radius:17px 0 0 17px}
.btn-clear{width:77px;height:34px;background:var(--white);color:#111;font:500 12px "Ubuntu",sans-serif;display:flex;align-items:center;justify-content:center}
.badge{left:958px;top:53px;width:17px;height:17px;border-radius:50%;background:var(--yellow);color:#222;font-size:9px;font-weight:700;display:flex;align-items:center;justify-content:center}
.avatar{left:995px;top:40px;width:41px;height:41px;border-radius:50%;border:2px solid var(--white);background:linear-gradient(135deg,#7a5a48,#3a2a24)}
.caret{left:1040px;top:58px}
.crumbs{left:161px;top:132px;display:flex;align-items:center;font-size:11px;font-weight:700;color:var(--white)}
.crumbs span{margin-right:24px}
.crumbs .sep{color:var(--muted);margin-right:6px;font-weight:400}
.crumbs .current{color:var(--orange)}

/* filter band */
.filter-band{left:0;top:170px;width:1200px;height:62px;background:var(--band-dark)}
.pill{height:33px;border-radius:17px;background:var(--field);display:flex;align-items:center;font-family:"Ubuntu",sans-serif;font-size:12px;color:var(--white)}
.search-users{left:150px;top:185px;width:285px;padding-left:47px}
.search-users svg{position:absolute;left:14px;top:9px}
.saved-filters{left:765px;top:185px;width:285px;padding-left:20px}
.saved-filters svg{position:absolute;right:14px;top:13px}

/* tabs */
.tab-band{left:0;top:232px;width:1200px;height:53px;background:var(--band-mid)}
.tab{top:232px;height:53px;display:flex;align-items:center;font-family:"Ubuntu",sans-serif;font-size:16px;color:var(--white)}
.tab.active{left:150px;width:89px;height:66px;background:var(--orange);justify-content:center;padding-bottom:13px}
.tab-fold{top:285px;width:0;height:0;border-top:12px solid var(--orange-dark)}
.create{left:887px;top:242px;width:163px;height:34px;border-radius:17px;background:var(--orange);font:500 14px "Ubuntu",sans-serif;color:var(--white);display:flex;align-items:center;padding-left:25px}
.create .plus{position:absolute;right:4px;top:4px;width:26px;height:26px;border-radius:50%;background:var(--white)}

/* posts */
.post{left:136px;width:914px}
.post-card{position:absolute;left:14px;top:0;width:900px;height:210px;background:var(--card)}
.post-photo{position:absolute;left:14px;top:0;width:115px;height:106px;background:radial-gradient(circle at 50% 55%,#c8c2b0 0%,#6c6a60 40%,#1c1c1c 75%)}
.post-author{position:absolute;left:0;top:106px;width:129px;height:29px;background:var(--orange);color:var(--white);font-size:11px;font-weight:700;padding-left:37px;line-height:29px}
.fold{position:absolute;width:0;height:0;border-left:14px solid transparent;border-bottom:10px solid var(--orange-dark)}
.post-title{position:absolute;left:159px;top:18px;font-family:"Ubuntu",sans-serif;font-size:14px;color:var(--orange)}
.post-body{position:absolute;left:159px;top:47px;width:740px;font-size:10.6px;line-height:18.75px;color:var(--text-light)}
.post-actions{position:absolute;left:159px;top:172px;display:flex;gap:14px;align-items:center}
.tagbar{position:absolute;left:0;top:210px;width:914px;height:29px;background:var(--tagbar);display:flex;align-items:center;font-size:10.5px;color:var(--white)}
.tagbar .tagicon{margin-left:27px;margin-right:16px}
.tag{background:var(--orange);padding:2px 4px;margin-right:11px;border:1px solid #ffbb55}
.stats{margin-left:auto;margin-right:15px;display:flex;align-items:center;gap:6px}
.stats .gap{width:14px}
.reply{position:absolute;left:14px;top:239px;width:900px;height:90px;background:var(--reply)}
.reply-photo{position:absolute;left:9px;top:11px;width:69px;height:69px;background:linear-gradient(160deg,#8aa0b8,#5a5a6a 50%,#3a3a3a)}
.reply-field{position:absolute;left:80px;top:11px;width:806px;height:66px;background:#403f41;padding:12px 13px;font-size:11.5px;font-weight:700;color:var(--white)}

/* footer */
.footer{left:0;top:998px;width:1200px;height:130px;background:var(--footer)}
.fcol{top:1020px;font-size:10px;font-weight:700;color:var(--white)}
.fcol h4{font-family:"Ubuntu",sans-serif;font-weight:500;font-size:13px;color:var(--muted);margin-bottom:12px}
.fcol li{list-style:none;line-height:17.5px;font-size:9.5px}
.fbrand{left:825px;top:1044px}
.to-top{left:1174px;top:1006px}
.footer-bottom{left:0;top:1128px;width:1200px;height:44px;background:var(--footer-bottom)}
.copy{left:150px;top:1145px;font-size:8.5px;color:#6c6c6c}
.social{top:1142px;width:16px;height:16px;border-radius:50%;background:#5c5c5c}
</style>
</head>
<body>

<header>
  <div class="abs brand"><span class="brand-mark"></span>Company Name</div>
  <div class="abs search-main">
    <svg width="16" height="16" viewBox="0 0 16 16"><circle cx="6.5" cy="6.5" r="5" fill="none" stroke="#ff9c00" stroke-width="2"/><line x1="10" y1="10" x2="15" y2="15" stroke="#ff9c00" stroke-width="2.5"/></svg>
    <span class="q">#northwind #bluepeak</span>
    <span class="btn-save">Save</span><span class="btn-clear">Clear</span>
  </div>
  <div class="abs badge">3</div>
  <div class="abs avatar" role="img" aria-label="Signed-in user profile photo"></div>
  <svg class="abs caret" width="10" height="6"><polygon points="0,0 10,0 5,6" fill="#ff9c00"/></svg>
  <nav class="abs crumbs">
    <svg width="14" height="12" viewBox="0 0 14 12" style="margin-right:8px"><polygon points="7,0 14,6 12,6 12,12 2,12 2,6 0,6" fill="#9a9a9a"/></svg>
    <span>Home</span><span class="sep">›</span><span>Conversations</span><span class="sep">›</span><span>Public</span><span class="sep">›</span><span class="current">#northwind#bluepeak</span>
  </nav>
</header>

<section class="abs filter-band"></section>
<div class="abs pill search-users">
  <svg width="16" height="16" viewBox="0 0 16 16"><circle cx="6.5" cy="6.5" r="5" fill="none" stroke="#fff" stroke-width="1.8"/><line x1="10" y1="10" x2="15" y2="15" stroke="#fff" stroke-width="2"/></svg>
  Search Users
</div>
<div class="abs pill saved-filters">Saved Filters
  <svg width="10" height="6"><polygon points="0,0 10,0 5,6" fill="#fff"/></svg>
</div>

<div class="abs tab-band"></div>
<div class="abs tab active">Public</div>
<div class="abs tab-fold" style="left:136px;border-left:14px solid transparent"></div>
<div class="abs tab-fold" style="left:239px;border-right:14px solid transparent"></div>
<div class="abs tab" style="left:274px">Following</div>
<div class="abs tab" style="left:402px">Contacts</div>
<div class="abs create">Create Thread<span class="plus"><svg width="26" height="26"><path d="M13 7v12M7 13h12" stroke="#333" stroke-width="2"/></svg></span></div>

<!-- thread 1 -->
<article class="abs post" style="top:338px">
  <div class="post-card"></div>
  <div class="post-photo" role="img" aria-label="Author avatar photo"></div>
  <div class="fold" style="left:0;top:96px"></div>
  <div class="post-author">Martin Hale</div>
  <div class="fold" style="left:0;top:200px"></div>
  <h2 class="post-title">Lorem ipsum subject</h2>
  <p class="post-body">Lorem ipsum dolor sit amet consecutor. Lorem ipsum dolor sit amet consecutor. Lorem ipsum dolor sit . Lorem ipsum dolor sit amet consecutor. Lorem ipsum dolor sit amet consecutor. Lorem ipsum dolor sit . Lorem ipsum dolor sit amet consecutor. Lorem ipsum dolor sit amet consecutor. Lorem ipsum dolor sit . Lorem ipsum dolor sit amet consecutor. Lorem ipsum dolor sit amet consecutor. Lorem ipsum dolor sit . Lorem ipsum dolor sit amet consecutor. Lorem ipsum dolor sit amet consecutor. Lorem ipsum dolor sit . Lorem ipsum dolor sit amet consecutor. Lorem ipsum dolor sit amet consecutor. Lorem ipsum dolor sit . Lorem ipsum dolor sit amet consecutor. Lorem ipsum dolor sit amet consecutor. Lorem ipsum dolor sit . Lorem ipsum dolor sit amet consecutor. Lorem ipsum dolor sit amet consecutor. Lorem ipsum dolor sit .</p>
  <div class="post-actions">
    <svg width="20" height="14"><path d="M8 1L1 7l7 6V9c5 0 8 1 11 4-1-5-4-8-11-8z" fill="#ff9c00"/></svg>
    <svg width="16" height="16"><polygon points="8,1 10,6 15,6 11,9.5 12.5,15 8,11.5 3.5,15 5,9.5 1,6 6,6" fill="#aaa"/></svg>
    <svg width="18" height="16"><rect x="1" y="2" width="16" height="13" fill="none" stroke="#aaa" stroke-width="1.5"/><path d="M1 6h16M5 9h2M9 9h2M13 9h2M5 12h2M9 12h2M13 12h2" stroke="#aaa"/></svg>
    <svg width="20" height="16"><ellipse cx="11" cy="7" rx="8" ry="6" fill="#aaa"/><path d="M4 10l-3 5 6-3z" fill="#aaa"/></svg>
  </div>
  <div class="tagbar">
    <svg class="tagicon" width="18" height="14"><path d="M1 1h7l7 7-6 6-8-8z" fill="#ccc"/></svg>
    <span class="tag">Technology</span><span class="tag">Education</span><span class="tag">Internet</span>
    <div class="stats">
      <svg width="20" height="14"><path d="M8 1L1 7l7 6V9c5 0 8 1 11 4-1-5-4-8-11-8z" fill="#aaa"/></svg>50<span class="gap"></span>
      <svg width="16" height="16"><polygon points="8,1 10,6 15,6 11,9.5 12.5,15 8,11.5 3.5,15 5,9.5 1,6 6,6" fill="#ff9c00"/></svg>101<span class="gap"></span>
      <svg width="18" height="16"><rect x="1" y="2" width="16" height="13" fill="none" stroke="#aaa" stroke-width="1.5"/><path d="M1 6h16" stroke="#aaa"/></svg>April 16, 2014<span class="gap"></span>
      <svg width="20" height="16"><ellipse cx="11" cy="7" rx="8" ry="6" fill="#aaa"/><path d="M4 10l-3 5 6-3z" fill="#aaa"/></svg>38 Comments
    </div>
  </div>
  <div class="reply">
    <div class="reply-photo" role="img" aria-label="Current user avatar photo"></div>
    <div class="reply-field">type your reply here</div>
  </div>
</article>

<!-- thread 2 -->
<article class="abs post" style="top:705px">
  <div class="post-card"></div>
  <div class="post-photo" role="img" aria-label="Author avatar photo"></div>
  <div class="fold" style="left:0;top:96px"></div>
  <div class="post-author">Martin Hale</div>
  <div class="fold" style="left:0;top:200px"></div>
  <h2 class="post-title">Lorem ipsum subject</h2>
  <p class="post-body">Lorem ipsum dolor sit amet consecutor. Lorem ipsum dolor sit amet consecutor. Lorem ipsum dolor sit . Lorem ipsum dolor sit amet consecutor. Lorem ipsum dolor sit amet consecutor. Lorem ipsum dolor sit . Lorem ipsum dolor sit amet consecutor. Lorem ipsum dolor sit amet consecutor. Lorem ipsum dolor sit . Lorem ipsum dolor sit amet consecutor. Lorem ipsum dolor sit amet consecutor. Lorem ipsum dolor sit . Lorem ipsum dolor sit amet consecutor. Lorem ipsum dolor sit amet consecutor. Lorem ipsum dolor sit . Lorem ipsum dolor sit amet consecutor. Lorem ipsum dolor sit amet consecutor. Lorem ipsum dolor sit . Lorem ipsum dolor sit amet consecutor. Lorem ipsum dolor sit amet consecutor. Lorem ipsum dolor sit . Lorem ipsum dolor sit amet consecutor. Lorem ipsum dolor sit amet consecutor. Lorem ipsum dolor sit .</p>
  <div class="post-actions">
    <svg width="20" height="14"><path d="M8 1L1 7l7 6V9c5 0 8 1 11 4-1-5-4-8-11-8z" fill="#ff9c00"/></svg>
    <svg width="16" height="16"><polygon points="8,1 10,6 15,6 11,9.5 12.5,15 8,11.5 3.5,15 5,9.5 1,6 6,6" fill="#aaa"/></svg>
    <svg width="18" height="16"><rect x="1" y="2" width="16" height="13" fill="none" stroke="#aaa" stroke-width="1.5"/><path d="M1 6h16M5 9h2M9 9h2M13 9h2M5 12h2M9 12h2M13 12h2" stroke="#aaa"/></svg>
    <svg width="20" height="16"><ellipse cx="11" cy="7" rx="8" ry="6" fill="#aaa"/><path d="M4 10l-3 5 6-3z" fill="#aaa"/></svg>
  </div>
  <div class="tagbar">
    <svg class="tagicon" width="18" height="14"><path d="M1 1h7l7 7-6 6-8-8z" fill="#ccc"/></svg>
    <span class="tag">Technology</span><span class="tag">Education</span><span class="tag">Internet</span>
    <div class="stats">
      <svg width="20" height="14"><path d="M8 1L1 7l7 6V9c5 0 8 1 11 4-1-5-4-8-11-8z" fill="#aaa"/></svg>50<span class="gap"></span>
      <svg width="16" height="16"><polygon points="8,1 10,6 15,6 11,9.5 12.5,15 8,11.5 3.5,15 5,9.5 1,6 6,6" fill="#ff9c00"/></svg>101<span class="gap"></span>
      <svg width="18" height="16"><rect x="1" y="2" width="16" height="13" fill="none" stroke="#aaa" stroke-width="1.5"/><path d="M1 6h16" stroke="#aaa"/></svg>April 16, 2014<span class="gap"></span>
      <svg width="20" height="16"><ellipse cx="11" cy="7" rx="8" ry="6" fill="#aaa"/><path d="M4 10l-3 5 6-3z" fill="#aaa"/></svg>38 Comments
    </div>
  </div>
</article>

<footer>
  <div class="abs footer"></div>
  <svg class="abs to-top" width="12" height="8"><polygon points="0,8 12,8 6,0" fill="#777"/></svg>
  <div class="abs fcol" style="left:152px"><h4>HEADING</h4><ul><li>DUMMY LINKS</li><li>DUMMY LINKS</li><li>DUMMY LINKS</li></ul></div>
  <div class="abs fcol" style="left:276px"><h4>HEADING</h4><ul><li>DUMMY LINKS</li><li>DUMMY LINKS</li><li>DUMMY LINKS</li></ul></div>
  <div class="abs fcol" style="left:395px"><h4>HEADING</h4><ul><li>DUMMY LINKS</li><li>DUMMY LINKS</li><li>DUMMY LINKS</li></ul></div>
  <div class="abs fcol" style="left:511px"><h4>HEADING</h4><ul><li>DUMMY LINKS</li><li>DUMMY LINKS</li><li>DUMMY LINKS</li></ul></div>
  <div class="abs fcol" style="left:632px"><h4>HEADING</h4><ul><li>DUMMY LINKS</li><li>DUMMY LINKS</li><li>DUMMY LINKS</li></ul></div>
  <div class="abs brand fbrand"><span class="brand-mark"></span>Company Name</div>
  <div class="abs footer-bottom"></div>
  <div class="abs copy ubuntu">© 2014 Company Name. All rights reserved.</div>
  <span class="abs social" style="left:986px"></span>
  <span class="abs social" style="left:1010px"></span>
  <span class="abs social" style="left:1034px"></span>
</footer>

</body>
</html>
```